Business card and stationery concept for weight management and nutrition practice
trueLeaf Guidance
Dear Designers,
I have uploaded my logo files and am looking forward to everyone's designs.
I would like to see designs that do not feature my logo quite so prominently - that is, the logo does not have to be very large.
Also, instead of bold abstract curves and shapes I'd like to see accents that are more feminine.
Thanks everyone!
I like the bold concepts you have uploaded. I would also like to see more simple ideas, using the light blue and dark grey used in the logo rather than black.
I would also like to see a few concepts that are a bit more feminine. Not overtly so but subtle.
Thank you!
I am unable to upload my logo at this time -- I will do this on Saturday evening when I get back in town.

```html
<!DOCTYPE html>
<html lang="en">
<head>
<meta charset="utf-8">
<title>trueLeaf Guidance – Business Card</title>
<link rel="stylesheet" href="https://fonts.googleapis.com/css2?family=Raleway:wght@400;500;600;700&display=swap">
<style>
  :root {
    --sky: #a7d5f2;
    --ink: #2f3336;
    --paper: #ffffff;
  }
  html, body {
    margin: 0;
    padding: 0;
    width: 1200px;
    height: 778px;
    overflow: hidden;
    background: var(--paper);
  }
  .card {
    position: relative;
    width: 1200px;
    height: 778px;
    background: var(--paper);
    color: var(--ink);
    font-family: "Raleway", sans-serif;
    overflow: hidden;
  }
  .card__wave {
    position: absolute;
    left: 0;
    top: 0;
    width: 1200px;
    height: 778px;
  }
  .card__wave path { fill: var(--sky); }

  .brand {
    position: absolute;
    right: 30px;
    top: 92px;
    display: flex;
    align-items: center;
    gap: 12px;
  }
  .brand__square {
    width: 22px;
    height: 22px;
    background: var(--sky);
  }
  .brand__name {
    font-size: 34px;
    font-weight: 600;
    line-height: 1;
    color: var(--ink);
  }

  .person {
    position: absolute;
    right: 597px;
    top: 330px;
    text-align: right;
  }
  .person__name {
    margin: 0;
    font-size: 70px;
    font-weight: 400;
    line-height: 1;
    letter-spacing: -0.5px;
    white-space: nowrap;
  }
  .person__name strong { font-weight: 700; }
  .person__credentials,
  .person__title {
    margin: 0;
    font-size: 33px;
    font-weight: 700;
    line-height: 1.4;
  }
  .person__credentials { margin-top: 20px; }

  .contact {
    position: absolute;
    right: 15px;
    top: 338px;
    text-align: right;
    font-size: 27px;
    font-weight: 500;
    line-height: 33px;
    font-style: normal;
  }
  .contact p { margin: 0; }
  .contact__gap { margin-top: 42px !important; }
</style>
</head>
<body>
  <main class="card">
    <svg class="card__wave" viewBox="0 0 1200 778" aria-hidden="true">
      <path d="M0 0 H500 C 720 250, 720 600, 512 778 H0 Z"/>
    </svg>

    <div class="brand">
      <span class="brand__square" aria-hidden="true"></span>
      <span class="brand__name">trueLeaf Guidance</span>
    </div>

    <section class="person">
      <h1 class="person__name">Maren J. <strong>Holloway</strong></h1>
      <p class="person__credentials">MS, RD, LDN</p>
      <p class="person__title">Registered Dietitian</p>
    </section>

    <address class="contact">
      <p>418 Willow Bend Road</p>
      <p>Fairmont, Illinois 61922</p>
      <p class="contact__gap">+91–98213–40768</p>
      <p>www.trueleafguidance.com</p>
      <p>trueleafguidance@gmail.com</p>
    </address>
  </main>
</body>
</html>
```